Amber Orchard Reverie Event Flyer - Fundraiser for a US Senate Candidate

Working on an event flyer for a fundraiser for a Concordant candidate for Senate in Tennessee. Hosting an event for him that's a Amber Orchard Reverie theme, and I need a cool flyer that fits the theme with event details.
Host names will be added to the flyer on an ongoing basis, so will need someone who can quickly add names to flyer as hosts commit. Would like to agree to a fee for all work up front.
I'm attaching a mockup of a flyer that my friend did, before he had to back out because of work commitments, as well as a couple of pieces of Amber Orchard Reverie art that I think are cool.
Concordant

```html
<!DOCTYPE html>
<html lang="en">
<head>
<meta charset="UTF-8">
<title>Summer Reception Flyer</title>
<link rel="stylesheet" href="https://fonts.googleapis.com/css2?family=Great+Vibes&family=Courgette&family=Open+Sans:wght@400;600&display=swap">
<style>
  :root {
    --page: #ecebe6;
    --night: #0b0d12;
    --dusk: #1e2a3c;
    --haze: #8d8a78;
    --moon: #d9cfb2;
    --ink: #ffffff;
    --ice: #cfe2f6;
    --soft: #e9e6dc;
  }
  * { margin: 0; padding: 0; box-sizing: border-box; }
  html, body { width: 1200px; height: 900px; overflow: hidden; background: var(--page); }
  .canvas { position: relative; width: 1200px; height: 900px; }
  .flyer {
    position: absolute; left: 280px; top: 30px; width: 640px; height: 840px;
    overflow: hidden; color: var(--ink); text-align: center;
    box-shadow: 0 12px 30px rgba(0,0,0,0.18);
  }
  .scene {
    position: absolute; inset: 0;
    background:
      radial-gradient(circle at 45% 52%, var(--moon) 0, rgba(217,207,178,0.55) 14%, rgba(141,138,120,0.2) 32%, transparent 50%),
      linear-gradient(180deg, var(--night) 0%, var(--dusk) 35%, #4a4b47 55%, #2a2c2c 72%, var(--night) 100%);
  }
  .invite { position: absolute; top: 56px; width: 100%; font: 24px "Courgette", cursive; }
  .title { position: absolute; top: 96px; width: 100%; font-family: "Great Vibes", cursive; line-height: 1; text-shadow: 0 2px 6px rgba(0,0,0,0.5); }
  .title .a { font-size: 104px; display: block; }
  .title .main { font-size: 114px; display: block; margin-top: -30px; }
  .title .sub { font-size: 96px; display: block; margin-top: -22px; }
  .title .sub .org { color: var(--ice); }
  .title .eve { font-size: 80px; display: block; margin-top: -30px; padding-left: 190px; }
  .details { position: absolute; top: 478px; width: 100%; font: 25px/1.3 "Courgette", cursive; }
  .details sup { font-size: 0.6em; line-height: 0; vertical-align: 0.6em; }
  .details .venue { margin-top: 20px; }
  .contribution { position: absolute; top: 662px; width: 100%; font: 15px/1.45 "Open Sans", sans-serif; color: var(--soft); }
  .contribution .rsvp { margin-top: 12px; }
  .footer { position: absolute; top: 778px; width: 100%; font: 600 13px "Open Sans", sans-serif; font-variant: small-caps; letter-spacing: 2px; }
  .sponsor-name { margin-top: 8px; display: inline-flex; align-items: center; gap: 8px; font: 600 16px "Open Sans", sans-serif; letter-spacing: 1px; }
  .sponsor-name .mark { width: 9px; height: 9px; background: var(--ink); }
</style>
</head>
<body>
<div class="canvas">
  <article class="flyer">
    <div class="scene" role="img" aria-label="Moonlit meadow at night framed by a large tree, with golden sparkles drifting through its branches"></div>
    <p class="invite">You're Cordially Invited to</p>
    <h1 class="title">
      <span class="a">A</span>
      <span class="main">Midsummer's</span>
      <span class="sub"><span class="org">Summit</span> Meeting</span>
      <span class="eve">Eve</span>
    </h1>
    <section class="details">
      <p>Reception for Daniel Whitcombe<br>Wednesday, August 23<sup>rd</sup> 6<sup>00</sup>–9<sup>00</sup>pm</p>
      <p class="venue">House of Lewis Carden<br>418B Alder Row, Nashville, TN 37290</p>
    </section>
    <section class="contribution">
      <p>Suggested Contribution:<br>$20.18 Friend | $100 Supporter | $250 Host</p>
      <p class="rsvp">RSVP at www.WhitcombeForTN.com/Midsummer or<br>RSVP by Email at RSVP@WhitcombeForTN.com</p>
    </section>
    <footer class="footer">
      <p>Paid for by Whitcombe for U.S. Senate</p>
      <div class="sponsor-name"><span class="mark"></span>Daniel Whitcombe</div>
    </footer>
  </article>
</div>
</body>
</html>
```